Creative Challenge - Disruptive Digital Construction Business needs an Application Design

We need an application design (4 screens).
The app will offer easy-to-use an interactive course to illustrate the latest technology to construction professionals. Kindly find the attachments.
Updates

I have just posted the contest and the deadline is tomorrow!! Please give me my original 7 days back.

Need extra days to review

Target Market(s)

Construction professionals, aged from 22 to 36, who want to learn new disruptive technologies in construction.

Colors
e667a6
b868aa
33a6d7

Requirements
Must have
• The name of the app, Velunor, stands for “Brightframe Skill Voyagers”. The user is a Velunor, who would transform the digital construction industry. We want a design that gives that feel to the users.

```html
<!DOCTYPE html>
<html lang="en">
<head>
<meta charset="utf-8">
<title>Velunor – App Screens</title>
<link href="https://fonts.googleapis.com/css2?family=Roboto:wght@400;500;700&display=swap" rel="stylesheet">
<style>
:root{
  --pink:#b868aa;
  --rose:#e667a6;
  --blue:#33a6d7;
  --grad:linear-gradient(90deg,#a55aa8 0%,#7a6fbf 50%,#3f94d8 100%);
  --ink:#222;
  --muted:#8a8a92;
  --line:#e3e3e8;
  --screen:#f3f3f6;
  --field:#ffffff;
}
*{box-sizing:border-box;margin:0;padding:0}
html,body{width:1200px;height:349px;overflow:hidden;background:#fff;font-family:'Roboto',sans-serif;color:var(--ink)}
.stage{position:absolute;left:0;top:0;width:2560px;height:745px;transform:scale(.46875);transform-origin:0 0}
.screen{position:absolute;top:45px;width:210px;background:var(--screen);border:1px solid #d6d6dc;border-radius:22px;overflow:hidden}
.abs{position:absolute;white-space:nowrap}
.wrap{white-space:normal}
.center{left:0;right:0;text-align:center}
.t6{font-size:6px}.t7{font-size:7px}.t8{font-size:8px}.t9{font-size:9.5px}.t10{font-size:10.5px}
.b{font-weight:700}.m{font-weight:500}
.muted{color:var(--muted)}
.field{position:absolute;left:12px;right:12px;height:24px;background:var(--field);border:1px solid #ececf0;border-radius:12px;font-size:7px;color:#999;padding-left:24px;line-height:22px}
.field::before{content:"";position:absolute;left:11px;top:8px;width:6px;height:6px;border-radius:1px;background:#c8c8d0}
.field.filled{color:#333}
.eye{position:absolute;right:10px;top:8px;width:10px;height:6px;border:1.1px solid #aaa;border-radius:50%}
.btn{position:absolute;left:14px;right:14px;height:28px;border-radius:14px;background:var(--grad);color:#fff;font-size:8.5px;font-weight:500;text-align:center;line-height:28px}
.btn.outline{background:#fff;border:1.2px solid var(--blue);color:var(--ink);line-height:25px}
.wordmark{font-size:20px;font-weight:700;letter-spacing:.5px;color:#1c1c22}
.photo{position:absolute;border-radius:6px;background:linear-gradient(160deg,#c7c9cc 0%,#9fa6ad 45%,#d8c46a 75%,#8a8f96 100%)}
.illus{position:absolute;background:linear-gradient(180deg,#f0f0f2,#d9dbe0);border-radius:8px}
.toggle{position:absolute;left:12px;width:20px;height:11px;border-radius:6px;border:1px solid #bbb;background:#fff}
.toggle::after{content:"";position:absolute;left:1px;top:1px;width:7px;height:7px;border-radius:50%;background:#ccc}
.toggle.on{background:var(--blue);border-color:var(--blue)}
.toggle.on::after{left:auto;right:1px;background:#fff}
.filter{position:absolute;right:12px;top:36px;width:10px;height:8px;border-top:1.1px solid #666;border-bottom:1.1px solid #666}
.filter::after{content:"";position:absolute;left:0;right:0;top:2.5px;border-top:1.1px solid #666}
.header{position:absolute;left:0;right:0;top:14px;height:24px}
.menu{position:absolute;left:12px;top:7px;width:9px;height:7px;border-top:1.3px solid #555;border-bottom:1.3px solid #555}
.menu::after{content:"";position:absolute;left:0;top:2px;width:6px;border-top:1.3px solid #555}
.search{position:absolute;left:34px;top:0;width:138px;height:22px;border-radius:5px;background:#e6e6ea;font-size:6.5px;color:#999;line-height:22px;padding-left:22px}
.search::before{content:"";position:absolute;left:9px;top:7px;width:6px;height:6px;border:1.2px solid #777;border-radius:50%}
.home{position:absolute;right:11px;top:5px;width:11px;height:10px;background:#6d66c4;clip-path:polygon(50% 0,100% 45%,88% 45%,88% 100%,12% 100%,12% 45%,0 45%)}
.title{position:absolute;left:12px;top:72px;font-size:9.5px;font-weight:700;white-space:nowrap}
.title span{color:var(--pink)}
.row{position:absolute;left:12px;right:12px;height:22px;border-radius:4px;background:#fff;font-size:6.5px;font-weight:500;line-height:22px;padding-left:24px;white-space:nowrap;box-shadow:0 1px 2px rgba(0,0,0,.06)}
.row::before{content:"";position:absolute;left:10px;top:7px;width:8px;height:8px;border-radius:1.5px;border:1.3px solid #6d66c4}
.row.active{background:var(--grad);color:#fff}
.row.active::before{border-color:#fff}
.chev{position:absolute;right:9px;top:8px;width:4px;height:4px;border-left:1.3px solid currentColor;border-top:1.3px solid currentColor;transform:rotate(45deg)}
.chev.down{transform:rotate(225deg);top:6px}
.progress{position:absolute;left:22px;width:120px;height:2px;background:#d8d8e0;border-radius:2px}
.progress::before{content:"";position:absolute;left:0;top:0;width:18px;height:2px;background:var(--pink);border-radius:2px}
.ptext{position:absolute;right:14px;font-size:5.5px;color:#777}
.rail{position:absolute;left:14px;width:1px;background:#cfcfd8}
.item{position:absolute;left:12px;right:12px;height:14px;font-size:8px;line-height:14px;padding-left:12px;color:#222;white-space:nowrap}
.item::before{content:"";position:absolute;left:0;top:5px;width:4px;height:4px;border-radius:50%;background:#bdbdc8}
.item.on::before{background:#6d66c4}
.item .chev{top:5px;right:0}
.card{position:absolute;width:74px;height:96px;background:#fff;border-radius:4px;box-shadow:0 1px 3px rgba(0,0,0,.08);font-size:7px;line-height:14px;padding:54px 0 0 8px;white-space:nowrap;overflow:hidden}
.card::before{content:"";position:absolute;left:8px;top:10px;width:34px;height:28px;border:1.3px solid #444;border-radius:2px}
.card::after{content:"";position:absolute;left:0;bottom:0;width:26px;height:2px;background:#6d66c4}
.back{position:absolute;left:12px;width:18px;height:18px;border-radius:50%;background:#fff;box-shadow:0 1px 3px rgba(0,0,0,.15)}
.back::after{content:"";position:absolute;left:7px;top:6px;width:4px;height:4px;border-left:1.3px solid #333;border-bottom:1.3px solid #333;transform:rotate(45deg)}
.heart{position:absolute;width:8px;height:7px;background:#7b5fc0;clip-path:polygon(50% 100%,0 40%,10% 5%,35% 0,50% 20%,65% 0,90% 5%,100% 40%)}
.play{position:absolute;width:24px;height:24px;border-radius:50%;background:rgba(120,100,200,.85)}
.play::after{content:"";position:absolute;left:9px;top:7px;border-left:8px solid #fff;border-top:5px solid transparent;border-bottom:5px solid transparent}
.lorem{position:absolute;left:12px;right:12px;font-size:6.5px;line-height:13px;color:#444}
.attach{position:absolute;left:12px;right:12px;height:22px;background:#fff;border-radius:6px;font-size:6px;line-height:22px;padding-left:22px;box-shadow:0 1px 2px rgba(0,0,0,.07)}
.attach::before{content:"";position:absolute;left:9px;top:7px;width:7px;height:7px;border:1.2px solid #6d66c4;border-radius:2px}
.attach::after{content:"↓";position:absolute;right:9px;top:0;color:#6d66c4;font-size:9px}
.drawer{position:absolute;left:0;top:0;bottom:0;width:155px;background:#fff}
.dim{position:absolute;left:155px;top:0;right:0;bottom:0;background:#a9a9ad}
.navitem{position:absolute;left:22px;font-size:6.5px;font-weight:500;padding-left:18px;line-height:10px;white-space:nowrap}
.navitem::before{content:"";position:absolute;left:0;top:2px;width:7px;height:6px;border-radius:1px;background:#cfcfd6}
.avatar{position:absolute;border-radius:50%;background:linear-gradient(135deg,#d9a58c,#7a4a3a)}
</style>
</head>
<body>
<div class="stage">

  <!-- Login -->
  <section class="screen" style="left:55px;height:452px;background:#fff">
    <div class="illus" role="img" aria-label="Illustration of construction workers reviewing plans beside a crane" style="left:22px;top:18px;width:166px;height:112px"></div>
    <div class="abs center wordmark" style="top:150px">VELUNOR</div>
    <div class="abs center t8 muted wrap" style="top:180px;line-height:13px">Welcome to<br>Brightframe Skill Voyagers</div>
    <div class="field filled" style="top:232px">name@mailbox.com</div>
    <div class="field" style="top:270px">Password<i class="eye"></i></div>
    <div class="abs t6 muted" style="left:22px;top:307px">Remember me?</div>
    <div class="abs t6" style="right:22px;top:307px;color:var(--blue)">Forget Password?</div>
    <div class="btn" style="top:322px">Login</div>
    <div class="abs center t7 muted" style="top:360px">Join Velunor community</div>
    <div class="btn outline" style="top:378px">Sign up with Proflux</div>
  </section>

  <!-- Sign up -->
  <section class="screen" style="left:305px;height:503px">
    <div class="back" style="top:26px"></div>
    <div class="abs center wordmark" style="top:22px">VELUNOR</div>
    <div class="abs t6" style="left:12px;top:73px">Personal Data</div>
    <div class="field filled" style="top:88px">Rian Tal</div>
    <div class="field" style="top:126px">Email</div>
    <div class="field" style="top:164px">Mobile phone</div>
    <div class="field" style="top:202px">Password</div>
    <div class="field" style="top:240px">Gender</div>
    <div class="abs t6" style="left:12px;top:282px">Profesional Personal Data</div>
    <div class="field" style="top:297px">Country</div>
    <div class="field" style="top:335px">Company name</div>
    <div class="field" style="top:373px">Title</div>
    <div class="field" style="top:411px">Years of expertise</div>
    <div class="btn" style="top:459px">Sign up</div>
  </section>

  <!-- Customize journey -->
  <section class="screen" style="left:555px;height:452px;background:#fff">
    <div class="abs t10 b" style="left:12px;top:33px">Customize Your Journey</div>
    <i class="filter"></i>
    <div class="abs t6 muted" style="left:12px;top:50px">(Show only the information activities related to you)</div>
    <div class="toggle on" style="top:94px"></div>
    <div class="abs t7" style="left:40px;top:95px;color:var(--blue)">I Am The Appointing Party</div>
    <div class="abs t6 muted" style="left:12px;top:111px">(You are the client / its representative)</div>
    <div class="toggle" style="top:133px"></div>
    <div class="abs t7" style="left:40px;top:134px">I Am The Lead Appointed Party</div>
    <div class="abs t6 muted" style="left:12px;top:150px">(You are the client / its representative)</div>
    <div class="toggle" style="top:172px"></div>
    <div class="abs t7" style="left:40px;top:173px">I Am The Appointed Party</div>
    <div class="abs t6 muted" style="left:12px;top:189px">(You are the client / its representative)</div>
    <div class="toggle" style="top:211px"></div>
    <div class="abs t7" style="left:40px;top:212px">Show Me All Information Management</div>
    <div class="abs t6 muted" style="left:12px;top:228px">(You are the client / its representative)</div>
    <div class="abs center t7" style="top:265px">You Might Custom</div>
    <div class="btn" style="top:403px">Next</div>
  </section>

  <!-- Home: How to start expanded -->
  <section class="screen" style="left:805px;height:452px">
    <div class="header"><i class="menu"></i><div class="search">Search</div><i class="home"></i></div>
    <div class="title">Your <span>Velunor</span> Journey Starts Here</div>
    <div class="row active" style="top:100px">How To Start BIM?<i class="chev down"></i></div>
    <div class="progress" style="top:133px"></div><div class="ptext" style="top:130px">Progress 10%</div>
    <div class="rail" style="top:160px;height:140px"></div>
    <div class="item on" style="top:154px">Aligment<i class="chev down"></i></div>
    <div class="card" style="left:26px;top:180px">PAS 1192 vs<br>ISO 19650</div>
    <div class="card" style="left:110px;top:180px">PAS 1192 vs<br>ISO 19650</div>
    <div class="card" style="left:194px;top:180px"></div>
    <div class="item" style="top:292px">Learning<i class="chev"></i></div>
    <div class="item" style="top:323px">Implementation<i class="chev"></i></div>
    <div class="row" style="top:360px">Information Management &nbsp;ISO 19650<i class="chev down"></i></div>
    <div class="row" style="top:396px">Resources<i class="chev"></i></div>
  </section>

  <!-- Home: ISO list -->
  <section class="screen" style="left:1055px;height:538px">
    <div class="header"><i class="menu"></i><div class="search">Search</div><i class="home"></i></div>
    <div class="title">Your <span>Velunor</span> Journey Starts Here</div>
    <div class="row" style="top:100px">How To Start BIM?<i class="chev"></i></div>
    <div class="row active" style="top:136px">Information Management &nbsp;ISO 19650<i class="chev down"></i></div>
    <div class="progress" style="top:169px"></div><div class="ptext" style="top:166px">Progress 10%</div>
    <div class="rail" style="top:196px;height:258px"></div>
    <div class="item" style="top:190px">ISO 19650 Principles<i class="chev"></i></div>
    <div class="item" style="top:221px">5.1 Assessment &amp; Need<i class="chev"></i></div>
    <div class="item" style="top:253px">5.2 Invitation To Tender<i class="chev"></i></div>
    <div class="item" style="top:284px">5.3 Tender Response<i class="chev"></i></div>
    <div class="item" style="top:316px">5.4 Appointment<i class="chev"></i></div>
    <div class="item" style="top:347px">5.5 Mobilization<i class="chev"></i></div>
    <div class="item" style="top:379px">5.6 Production Of Information<i class="chev"></i></div>
    <div class="item" style="top:410px">5.7 Information Model Delivery<i class="chev"></i></div>
    <div class="item" style="top:442px">5.8. Project Close-Out<i class="chev"></i></div>
    <div class="row" style="top:479px">Resources<i class="chev"></i></div>
  </section>

  <!-- Home: principles expanded -->
  <section class="screen" style="left:1305px;height:648px">
    <div class="header"><i class="menu"></i><div class="search">Search</div><i class="home"></i></div>
    <div class="title">Your <span>Velunor</span> Journey Starts Here</div>
    <div class="row" style="top:100px">How To Start BIM?<i class="chev"></i></div>
    <div class="row active" style="top:136px">Information Management &nbsp;ISO 19650<i class="chev down"></i></div>
    <div class="progress" style="top:169px"></div><div class="ptext" style="top:166px">Progress 10%</div>
    <div class="rail" style="top:196px;height:364px"></div>
    <div class="item on" style="top:190px">ISO 19650 Principles<i class="chev down"></i></div>
    <div class="card" style="left:26px;top:215px">PAS 1192 vs<br>ISO 19650</div>
    <div class="card" style="left:110px;top:215px">PAS 1192 vs<br>ISO 19650</div>
    <div class="card" style="left:194px;top:215px"></div>
    <div class="item" style="top:328px">5.1 Assessment &amp; Need<i class="chev"></i></div>
    <div class="item" style="top:359px">5.2 Invitation To Tender<i class="chev"></i></div>
    <div class="item" style="top:391px">5.3 Tender Response<i class="chev"></i></div>
    <div class="item" style="top:422px">5.4 Appointment<i class="chev"></i></div>
    <div class="item" style="top:454px">5.5 Mobilization<i class="chev"></i></div>
    <div class="item" style="top:485px">5.6 Production Of Information<i class="chev"></i></div>
    <div class="item" style="top:517px">5.7 Information Model Delivery<i class="chev"></i></div>
    <div class="item" style="top:548px">5.8. Project Close-Out<i class="chev"></i></div>
    <div class="row" style="top:585px">Resources<i class="chev"></i></div>
  </section>

  <!-- Home: resources -->
  <section class="screen" style="left:1555px;height:452px">
    <div class="header"><i class="menu"></i><div class="search">Search</div><i class="home"></i></div>
    <div class="title">Your <span>Velunor</span> Journey Starts Here</div>
    <div class="row" style="top:100px">How To Start BIM?<i class="chev"></i></div>
    <div class="row active" style="top:136px">Information Management &nbsp;ISO 19650<i class="chev down"></i></div>
    <div class="row" style="top:172px">Resources<i class="chev"></i></div>
    <div class="progress" style="top:205px"></div><div class="ptext" style="top:202px">Progress 10%</div>
    <div class="item on" style="top:225px">Abbreviations<i class="chev"></i></div>
    <div class="item" style="top:257px">References<i class="chev"></i></div>
    <div class="item" style="top:289px">BIM Software<i class="chev"></i></div>
    <div class="item" style="top:320px">Useful Links<i class="chev"></i></div>
  </section>

  <!-- Video description -->
  <section class="screen" style="left:1805px;height:553px;background:#fff">
    <div class="back" style="top:17px"></div>
    <div class="abs center t10 m" style="top:20px">Video Description</div>
    <div class="abs t6" style="left:12px;top:70px;color:var(--blue)">Appointment Level</div>
    <i class="heart" style="right:14px;top:70px"></i>
    <div class="abs t9 b wrap" style="left:12px;top:86px;right:10px;line-height:15px">5.1.1 Appoint Individuals To Undertake The Information Management Function</div>
    <div class="abs t6 muted" style="left:12px;top:128px">(Information Procurement Stage)</div>
    <div class="abs t6 muted" style="left:12px;top:143px"><span style="color:var(--blue)">Actor:</span> The Lead Appointed Party</div>
    <div class="photo" role="img" aria-label="Video still of engineers in hard hats on a construction site" style="left:10px;top:173px;width:190px;height:110px"></div>
    <i class="play" style="left:93px;top:215px"></i>
    <div class="abs t7 b" style="left:12px;top:305px">Description :</div>
    <div class="lorem" style="top:321px">Lorem ipsum dolor sit amet, consetetur ing elitr, sed diam nonumy eirmod tempor invidunt ut labore et dolore magna aliquyam erat, sed diam</div>
    <div class="abs t6" style="left:140px;top:381px;width:62px;height:19px;border-radius:10px;background:var(--grad);color:#fff;text-align:center;line-height:19px">Start →</div>
    <div class="abs t7 m" style="left:12px;top:434px">Attachment</div>
    <div class="attach" style="top:456px">Lorem Ipsum Ser Dolor Amet</div>
    <div class="attach" style="top:492px">Lorem Ipsum Ser Dolor Amet</div>
  </section>

  <!-- Lesson detail -->
  <section class="screen" style="left:2055px;height:452px;background:#fff">
    <div class="abs" style="left:0;right:0;top:0;height:165px;background:linear-gradient(160deg,#a55aa8 0%,#7a6fbf 45%,#3f94d8 100%);border-radius:0 0 18px 18px"></div>
    <div class="back" style="top:16px"></div>
    <div class="abs t6" style="left:12px;top:57px;color:#fff">Appointment Level</div>
    <div class="abs t9 b wrap" style="left:12px;top:74px;right:10px;line-height:15px;color:#fff">5.1.1 Appoint Individuals To Undertake The Information Management Function</div>
    <div class="abs t6" style="left:12px;top:115px;color:#eee">(Information Procurement Stage)</div>
    <div class="abs t6" style="left:12px;top:130px;color:#fff">Actor: The Lead Appointed Party</div>
    <div class="photo" role="img" aria-label="Video still of engineers in hard hats on a construction site" style="left:10px;top:187px;width:190px;height:118px"></div>
    <i class="play" style="left:93px;top:234px;background:rgba(230,103,166,.9)"></i>
    <div class="abs t7 b" style="left:12px;top:328px">Description :</div>
    <i class="heart" style="right:18px;top:328px"></i>
    <div class="lorem" style="top:344px">Lorem ipsum dolor sit amet, consetetur ing elitr, sed diam nonumy eirmod tempor invidunt ut labore et dolore magna aliquyam erat, sed diam</div>
    <div class="abs" style="left:0;right:0;top:425px;height:27px;background:var(--grad);color:#fff;font-size:9px;font-weight:500;text-align:center;line-height:27px">‹ 02 / 06 ›</div>
  </section>

  <!-- Side drawer -->
  <section class="screen" style="left:2305px;height:452px">
    <div class="dim"><div class="abs t9 b" style="left:4px;top:70px;color:#222">Here</div></div>
    <div class="avatar" role="img" aria-label="Profile photo" style="left:182px;top:14px;width:20px;height:20px"></div>
    <div class="drawer">
      <div class="abs" style="left:0;right:0;top:0;height:58px;background:var(--grad)"></div>
      <div class="avatar" role="img" aria-label="Profile photo" style="left:18px;top:20px;width:20px;height:20px"></div>
      <div class="abs t7 b" style="left:46px;top:22px;color:#fff">Mara</div>
      <div class="abs" style="left:46px;top:32px;color:#fff;font-size:4.5px">Harbor City, NV</div>
      <div class="navitem" style="top:76px">My favorite</div>
      <div class="navitem" style="top:102px">Search</div>
      <div class="navitem" style="top:129px">About the app</div>
      <div class="navitem" style="top:156px">About the authors</div>
      <div class="navitem" style="top:182px">Setting</div>
      <div class="navitem" style="top:434px">Log out</div>
    </div>
  </section>

</div>
</body>
</html>
```